Postcard Design

Marlow Painting-all types of painting and staining-house,deck and roof powerwashing-stone and masonry sealing-
30 years in business-licensed and insured
Ray Marlow
Marlowtrio@quillnet.com
5076182243

Industry/Entity Type

Painting

```html
<!DOCTYPE html>
<html lang="en">
<head>
<meta charset="utf-8">
<title>Marlow Painting Postcard</title>
<link rel="stylesheet" href="https://fonts.googleapis.com/css2?family=Exo+2:wght@300;400;600&family=Open+Sans:wght@400;600;700&display=swap">
<style>
  :root {
    --stage: #3a3a3c;
    --purple: #5a4677;
    --purple-dark: #443358;
    --purple-band: #4d3b66;
    --ink: #231c2c;
    --gold: #f2c64a;
    --gold-deep: #e0a82a;
    --white: #ffffff;
    --paper: #fbfbfb;
    --stamp: #eeeeee;
    --rule: #e2e2e2;
    --brand: #5b4a86;
    --art-light: #fbf3ec;
    --art-warm: #f3c9a4;
    --photo-sky: #6f9fd6;
    --photo-wall: #c9b28c;
  }
  * { box-sizing: border-box; margin: 0; padding: 0; }
  html, body { width: 1200px; height: 887px; overflow: hidden; }
  body {
    position: relative;
    background: var(--stage);
    font-family: "Open Sans", Arial, sans-serif;
  }
  .view-label {
    position: absolute;
    color: var(--white);
    font-weight: 700;
    font-size: 25px;
    letter-spacing: 0.5px;
    line-height: 1;
  }
  .view-label--front { left: 633px; top: 55px; }
  .view-label--back { left: 406px; top: 817px; }

  /* ---------- Front ---------- */
  .card-front {
    position: absolute; left: 48px; top: 25px;
    width: 542px; height: 400px;
    background: var(--white); overflow: hidden;
  }
  .front-topband { position: absolute; left: 0; top: 0; width: 100%; height: 17px; background: var(--purple); }
  .front-artwork {
    position: absolute; left: 0; top: 17px; width: 100%; height: 236px;
    background: linear-gradient(180deg, var(--art-light) 0%, var(--art-warm) 100%);
  }
  .brand {
    position: absolute; display: flex; align-items: center; gap: 8px;
    font-family: "Exo 2", Arial, sans-serif; font-weight: 600; color: var(--brand);
    line-height: 1;
  }
  .brand__mark { width: 12px; height: 12px; background: currentColor; }
  .card-front .brand { left: 22px; top: 76px; font-size: 22px; }
  .badge {
    position: absolute; height: 24px; display: flex; align-items: center;
    padding: 0 18px 0 38px; border-radius: 4px;
    background: linear-gradient(var(--gold), var(--gold-deep));
    color: var(--ink); font-size: 14px; line-height: 1;
  }
  .badge strong { font-weight: 700; }
  .badge .gap { margin: 0 4px; }
  .badge__tick {
    position: absolute; left: -4px; top: -3px; width: 30px; height: 30px;
  }
  .badge--years { left: 282px; top: 137px; }
  .badge--license { left: 335px; top: 177px; }
  .front-strip {
    position: absolute; left: 0; top: 253px; width: 100%; height: 25px;
    background: var(--ink);
  }
  .front-strip__tagline {
    position: absolute; left: 16px; top: 6px; line-height: 1;
    color: var(--gold); font-size: 13px; font-weight: 600; letter-spacing: 1px;
  }
  .front-strip__owner {
    position: absolute; left: 242px; top: -4px; width: 154px; height: 29px;
    background: linear-gradient(var(--gold), var(--gold-deep));
    border-radius: 6px 6px 0 0;
    color: var(--ink); font-weight: 700; font-size: 15px; letter-spacing: 1.5px;
    display: flex; align-items: center; justify-content: center;
  }
  .front-panel {
    position: absolute; left: 0; top: 278px; width: 100%; height: 122px;
    background: linear-gradient(180deg, var(--purple), var(--purple-band));
    color: var(--white);
  }
  .panel-title {
    font-family: "Exo 2", Arial, sans-serif; font-weight: 400;
    font-size: 23px; letter-spacing: .3px; line-height: 1;
  }
  .front-about { position: absolute; left: 18px; top: 8px; width: 215px; }
  .front-about p { font-size: 8.5px; line-height: 1.3; margin-top: 4px; }
  .front-divider { position: absolute; left: 239px; top: 8px; width: 2px; height: 52px; background: var(--white); }
  .front-services { position: absolute; left: 252px; top: 8px; }
  .service-list { list-style: none; font-size: 8.5px; line-height: 1.3; margin-top: 3px; }
  .service-list li::before { content: "\25CF"; margin-right: 11px; font-size: 6px; vertical-align: 1px; }
  .front-contact {
    position: absolute; left: 0; top: 83px; width: 100%; height: 22px;
    background: var(--purple-dark);
    display: flex; align-items: center; justify-content: flex-end; gap: 18px;
    padding-right: 10px;
  }
  .contact { display: flex; align-items: center; gap: 6px; line-height: 1; }
  .contact--phone { font-weight: 700; font-size: 19px; letter-spacing: 1.5px; }
  .contact--mail { font-size: 14px; }

  /* ---------- Back ---------- */
  .card-back {
    position: absolute; left: 615px; top: 438px;
    width: 543px; height: 418px; background: var(--paper); overflow: hidden;
  }
  .back-panel { position: absolute; left: 0; top: 0; width: 262px; height: 348px; background: var(--purple); color: var(--white); }
  .back-photo {
    position: absolute; left: 0; top: 0; width: 100%; height: 218px;
    background: linear-gradient(180deg, var(--photo-sky) 0%, var(--photo-wall) 100%);
  }
  .card-back .brand { right: 18px; top: 36px; font-size: 15px; color: var(--white); }
  .back-rainbow {
    position: absolute; left: 0; top: 218px; width: 100%; height: 5px;
    background: linear-gradient(90deg, #7c3fa0, #d2397a, #f0812d, #f4c534);
  }
  .back-copy { position: absolute; left: 15px; top: 228px; }
  .back-copy .panel-title { font-size: 21px; }
  .back-copy .panel-subtitle {
    font-family: "Exo 2", Arial, sans-serif; font-weight: 600;
    font-size: 18px; line-height: 1; margin-top: 1px;
  }
  .back-copy .service-list { font-size: 8px; line-height: 1.25; margin-top: 3px; }
  .back-copy .contact--phone { margin-top: 14px; font-size: 28px; letter-spacing: 2.5px; gap: 12px; }
  .stamp-box { position: absolute; left: 450px; top: 14px; width: 78px; height: 88px; background: var(--stamp); }
  .address-line { position: absolute; left: 305px; width: 220px; height: 1px; background: var(--rule); }
</style>
</head>
<body>
  <div class="view-label view-label--front">FRONT DESIGN</div>
  <div class="view-label view-label--back">BACK DESIGN</div>

  <section class="card-front">
    <div class="front-topband"></div>
    <div class="front-artwork" role="img" aria-label="Abstract flowing ribbons of multicoloured paint"></div>
    <div class="brand"><span class="brand__mark"></span>Marlow Painting</div>

    <div class="badge badge--years">
      <svg class="badge__tick" viewBox="0 0 30 30"><circle cx="15" cy="15" r="15" fill="#231c2c"/><path d="M9 15l4 5 8-11" stroke="#f2c64a" stroke-width="3" fill="none"/></svg>
      <strong>30 years</strong><span class="gap">in business</span>
    </div>
    <div class="badge badge--license">
      <svg class="badge__tick" viewBox="0 0 30 30"><circle cx="15" cy="15" r="15" fill="#231c2c"/><path d="M9 15l4 5 8-11" stroke="#f2c64a" stroke-width="3" fill="none"/></svg>
      <strong>Licensed</strong><span class="gap">and</span><strong>Insured</strong>
    </div>

    <div class="front-strip">
      <span class="front-strip__tagline">PROFESSIONAL HOME SERVICES</span>
      <span class="front-strip__owner">Ray Marlow</span>
    </div>

    <div class="front-panel">
      <div class="front-about">
        <h2 class="panel-title">MARLOW PAINTING</h2>
        <p>Professional Home Services specializes in exterior, residential and commercial painting projects</p>
      </div>
      <div class="front-divider"></div>
      <div class="front-services">
        <h2 class="panel-title">OUR SERVICE</h2>
        <ul class="service-list">
          <li>all types of painting and staining</li>
          <li>house,deck and roof powerwashing</li>
          <li>stone and masonry sealing</li>
        </ul>
      </div>
      <div class="front-contact">
        <span class="contact contact--phone">
          <svg width="17" height="17" viewBox="0 0 20 20"><circle cx="10" cy="10" r="9" fill="none" stroke="#fff" stroke-width="1.5"/><path d="M7 5c-1 1-1 3 1 6s4 4 5 3l1-1-2-2-1 1c-1-.5-2-1.5-2.5-2.5l1-1-2-2z" fill="#fff"/></svg>
          5076182243
        </span>
        <span class="contact contact--mail">
          <svg width="16" height="11" viewBox="0 0 16 11"><rect x=".5" y=".5" width="15" height="10" fill="none" stroke="#fff"/><path d="M.5 .5l7.5 6 7.5-6" fill="none" stroke="#fff"/></svg>
          Marlowtrio@quillnet.com
        </span>
      </div>
    </div>
  </section>

  <section class="card-back">
    <div class="back-panel">
      <div class="back-photo" role="img" aria-label="Photo of a two-storey house under a blue sky"></div>
      <div class="brand"><span class="brand__mark"></span>Marlow Painting</div>
      <div class="back-rainbow"></div>
      <div class="back-copy">
        <h2 class="panel-title">MARLOW PAINTING</h2>
        <h3 class="panel-subtitle">OUR SERVICE</h3>
        <ul class="service-list">
          <li>all types of painting and staining</li>
          <li>house,deck and roof powerwashing</li>
          <li>stone and masonry sealing</li>
        </ul>
        <span class="contact contact--phone">
          <svg width="24" height="24" viewBox="0 0 20 20"><circle cx="10" cy="10" r="9" fill="none" stroke="#fff" stroke-width="1.5"/><path d="M7 5c-1 1-1 3 1 6s4 4 5 3l1-1-2-2-1 1c-1-.5-2-1.5-2.5-2.5l1-1-2-2z" fill="#fff"/></svg>
          5076182243
        </span>
      </div>
    </div>
    <div class="stamp-box"></div>
    <div class="address-line" style="top:250px"></div>
    <div class="address-line" style="top:270px"></div>
    <div class="address-line" style="top:292px"></div>
    <div class="address-line" style="top:315px"></div>
  </section>
</body>
</html>
```